Business card for someone who trains leaders
Organizational Development Consultant Business Card - Consulting
Organizational Development Consultant Business Card
Bright & Fun-filled
Darla Quinby
Capacity Development Adviser
(NO ADDRESS IS LISTED ON CARD)
darla@vrmthrivewell.com
www.netprofile/in/marlowquinby
I want a business card that says professional but not too corporate. I want it to only use the colors on my logo (plus white of course). I like the look of cards that have some black backgrounds, but I'm open to a lot of different looks - as long as it meshes well with the look and feel of the business card. I don't want anything too busy, but yet want something that stands out a bit.
Where Will Your Growth Lead? Let VRM Thrivewell help you find growth through organizational development, leadership coaching, and much more!
marlowquinby marlowquinby
Please don't submit generic samples with someone else's information. I'm only interested in seeing completed business cards with the information I included in the creative brief.
I would like to see some designs that are on a white background as well as a black background. I'm not sold either way, but want to see a variety. Also, on the creative brief, I left off the website. In addition to my netprofile profile, I also want the website www.vrmthrivewell.com.

```html
<!DOCTYPE html>
<html lang="en">
<head>
<meta charset="utf-8">
<title>VRM Thrivewell – Business Card</title>
<link href="https://fonts.googleapis.com/css2?family=Open+Sans:wght@400;600;700&display=swap" rel="stylesheet">
<style>
  :root{
    --stage:#8a8a8a;
    --purple:#7a3d9e;
    --purple-soft:#b99ad0;
    --blue:#2e86d6;
    --blue-soft:#a9c6ec;
    --slate:#5d6470;
    --smoke:#6f7278;
    --ink:#3a3d44;
    --white:#ffffff;
  }
  *{box-sizing:border-box;margin:0;padding:0}
  html,body{width:1200px;height:908px;overflow:hidden}
  body{background:var(--stage);font-family:"Open Sans",Arial,sans-serif;position:relative}
  .card{position:absolute;top:284px;width:540px;height:340px;border-radius:18px;overflow:hidden}
  .card--back{left:50px;background:linear-gradient(135deg,#7c7f85,var(--smoke) 60%,#65686e)}
  .card--front{left:610px;background:var(--white)}
  .deco{position:absolute;border-radius:50%}
  .card--back .deco{right:-40px;top:20px;width:280px;height:280px;
    background:radial-gradient(circle at 40% 35%,rgba(169,198,236,.55),rgba(185,154,208,.45) 60%,rgba(255,255,255,.12))}
  .card--front .deco{right:-30px;top:-50px;width:240px;height:240px;
    background:radial-gradient(circle at 40% 40%,rgba(169,198,236,.45),rgba(185,154,208,.3) 60%,rgba(230,230,240,.35))}
  .brand{position:absolute;display:flex;align-items:center;gap:10px}
  .brand__dot{width:38px;height:38px;border-radius:50%;background:var(--purple)}
  .brand__name{font-weight:700;font-size:25px;letter-spacing:.5px;color:var(--blue);text-transform:uppercase;line-height:1}
  .brand__tagline{font-size:12px;color:var(--purple);margin-top:4px;border-top:1px solid var(--purple-soft);padding-top:3px}
  .card--back .brand{left:34px;top:76px}
  .card--back .brand__name{font-size:28px;color:var(--white)}
  .card--back .brand__tagline{color:#e9e0f2}
  .pitch{position:absolute;left:34px;top:150px;width:270px;color:var(--white);font-size:14px;line-height:1.45}
  .card--front .brand{left:60px;top:120px}
  .accent-square{position:absolute;left:0;top:96px;width:30px;height:30px;background:var(--blue)}
  .person{position:absolute;left:150px;top:190px}
  .person__name{font-size:20px;font-weight:600;color:var(--blue);line-height:1.1}
  .person__role{font-size:13px;font-weight:700;color:var(--purple)}
  .purple-band{position:absolute;left:0;top:236px;width:135px;height:56px;background:var(--purple)}
  .contacts{position:absolute;left:150px;top:238px;list-style:none;font-size:12.5px;color:var(--ink);line-height:1.55}
  .contacts li{display:flex;align-items:center;gap:7px}
  .contacts svg{width:12px;height:12px;flex:none}
</style>
</head>
<body>
  <section class="card card--back" aria-label="Card back">
    <div class="deco"></div>
    <div class="brand">
      <div>
        <div class="brand__name">VRM Thrivewell</div>
        <div class="brand__tagline">Where Will Your Growth Lead?</div>
      </div>
    </div>
    <p class="pitch">Let VRM Thrivewell help you find growth through organizational development, leadership coaching, and much more!</p>
  </section>

  <section class="card card--front" aria-label="Card front">
    <div class="deco"></div>
    <div class="accent-square"></div>
    <div class="brand">
      <div class="brand__dot"></div>
      <div>
        <div class="brand__name">VRM Thrivewell</div>
        <div class="brand__tagline">Where Will Your Growth Lead?</div>
      </div>
    </div>
    <div class="person">
      <div class="person__name">Darla Quinby</div>
      <div class="person__role">Capacity Development Adviser</div>
    </div>
    <div class="purple-band"></div>
    <ul class="contacts">
      <li><svg viewBox="0 0 12 12"><path d="M3 1l2 2-1 1.5c.6 1.4 1.6 2.4 3 3L8.5 6.5l2 2L9 10.5C5 10 2 7 1.5 3z" fill="var(--purple)"/></svg>435-555-0142</li>
      <li><svg viewBox="0 0 12 12"><rect x="1" y="2.5" width="10" height="7" fill="var(--purple)"/><path d="M1 2.5l5 4 5-4" stroke="#fff" fill="none"/></svg>darla@vrmthrivewell.com</li>
      <li><svg viewBox="0 0 12 12"><rect x="1" y="1" width="10" height="10" rx="2" fill="var(--purple)"/></svg>www.netprofile/in/marlowquinby</li>
      <li><svg viewBox="0 0 12 12"><circle cx="6" cy="6" r="5" fill="var(--purple)"/><path d="M1 6h10M6 1c-2.5 3-2.5 7 0 10M6 1c2.5 3 2.5 7 0 10" stroke="#fff" stroke-width=".8" fill="none"/></svg>www.vrmthrivewell.com</li>
    </ul>
  </section>
</body>
</html>
```